iOS App Design - Google Material Design + Sketch

What we would love to do is to create an activity feed page plus main navigation for our iOS application. If we like this design then we'd like to hire someone to take the design elements and build out the rest of our screens.

The design must use Google Material Design and be delivered in a Sketch file.

Our product is an application for activity provider owners to manage their daily business while on the go. This activity feed/home screen will provide them with information about their bookings, tours that day, etc.

We would like for it to be modern and eye catching, yet simple and functional for someone to use outdoors and while not in an office.

For this home screen, the main elements we would like to include:

- Main App Navigation with 4 elements: Home, Availability/Calendar, Booking and Settings
- A way to add a booking (plus sign or similar that is a constant - nav or floating

- A couple of overall key metrics that indicate how you the user’s business is doing that month that are static - not part of the feed

- A way to show different types of activity in a "news feed" - i.e. if a booking has happened or there is an upcoming tour, if a payment has been made to your account, suggestion on how to improve your profile.

- A way to filter the activities

We are open to the layout and options for these main elements above, we would like your opinion on how best from a user design perspective we can implement these.

Please let us know if you have any questions.

```html
<!DOCTYPE html>
<html lang="en">
<head>
<meta charset="utf-8">
<title>My Business – Home</title>
<link rel="stylesheet" href="https://fonts.googleapis.com/css2?family=Crimson+Text:wght@400;600&family=Roboto:wght@400;700&display=swap">
<style>
  :root {
    --page-bg: #e4e4e4;
    --screen-bg: #ededed;
    --ink: #111111;
    --muted: #9a9a9a;
    --rule: #cfcfcf;
    --tile-dark: #343a45;
    --tile-slate: #6a7d8c;
    --bar-lime: #cfdd35;
    --bar-green: #93bf4b;
    --icon-grey: #6b6b6b;
  }
  * { box-sizing: border-box; margin: 0; padding: 0; }
  html, body {
    width: 1177px; height: 1200px; overflow: hidden;
    background: var(--page-bg);
  }
  .app-screen {
    position: absolute; left: 273px; top: 40px;
    width: 630px; height: 1120px;
    background: var(--screen-bg);
    box-shadow: 0 10px 40px rgba(0,0,0,.12);
    font-family: "Crimson Text", Georgia, serif;
    color: var(--ink);
    overflow: hidden;
  }
  .status-bar {
    height: 40px; display: flex; align-items: center; justify-content: space-between;
    padding: 0 18px; font-family: "Roboto", Arial, sans-serif; font-size: 15px;
  }
  .status-bar .signal { display: flex; gap: 3px; align-items: center; }
  .status-bar .signal span { width: 8px; height: 8px; border-radius: 50%; background: var(--ink); }
  .status-bar .signal span.off { background: none; border: 1px solid var(--ink); }
  .status-bar .battery { display: flex; align-items: center; gap: 5px; }
  .battery-cell { width: 34px; height: 14px; border: 1px solid var(--ink); padding: 1px; }
  .battery-cell i { display: block; height: 100%; background: var(--ink); }

  .app-header {
    height: 90px; position: relative;
    display: flex; align-items: center; justify-content: center;
  }
  .app-header .title { font-size: 36px; font-weight: 600; display: flex; align-items: center; gap: 10px; }
  .app-header .back { position: absolute; left: 22px; top: 26px; }
  .app-header .add-booking { position: absolute; right: 22px; top: 18px; }

  .metric-tiles { display: flex; height: 200px; }
  .metric-tile {
    flex: 1; color: #fff; font-size: 62px; line-height: 1;
    padding: 34px 30px;
  }
  .metric-tile.budget { background: var(--tile-dark); }
  .metric-tile.profit { background: var(--tile-slate); }

  .stats-tabs {
    display: flex; justify-content: center; align-items: baseline; gap: 12px;
    margin-top: 32px;
  }
  .stats-tabs .active { font-family: "Roboto", Arial, sans-serif; font-weight: 700; font-size: 19px; }
  .stats-tabs .tab { font-size: 17px; }

  .stats-chart { display: block; margin-top: 6px; }
  .stats-chart text { font-family: "Roboto", Arial, sans-serif; }

  .range-filter {
    display: flex; justify-content: center; align-items: baseline; gap: 40px;
    padding: 10px 0 20px; font-size: 20px;
    border-bottom: 1px solid var(--rule); margin: 0 30px;
  }
  .range-filter .active { font-family: "Roboto", Arial, sans-serif; font-weight: 700; font-size: 21px; }

  .feed-row {
    height: 80px; margin: 0 30px; border-bottom: 1px solid var(--rule);
    display: flex; align-items: center; justify-content: space-between;
  }
  .feed-row .label { font-size: 32px; }
  .feed-row .amount { font-size: 50px; }
  .feed-row.booking .label { font-size: 40px; padding-left: 10px; }

  .tab-bar {
    position: absolute; left: 0; bottom: 0; width: 100%; height: 100px;
    display: flex; border-top: 1px solid var(--rule);
  }
  .tab-bar .nav-item {
    flex: 1; display: flex; align-items: center; justify-content: center;
    border-right: 2px solid var(--rule);
  }
  .tab-bar .nav-item:last-child { border-right: none; }
</style>
</head>
<body>
<main class="app-screen">
  <div class="status-bar">
    <div class="signal">
      <span></span><span></span><span></span><span></span><span class="off"></span>
      <svg width="18" height="14" viewBox="0 0 18 14" style="margin-left:6px"><path d="M1 5a11 11 0 0 1 16 0M4 8a7 7 0 0 1 10 0M7 11a3 3 0 0 1 4 0" fill="none" stroke="#111" stroke-width="1.8"/></svg>
    </div>
    <div class="time">4:34</div>
    <div class="battery">100% <span class="battery-cell"><i></i></span></div>
  </div>

  <header class="app-header">
    <svg class="back" width="40" height="34" viewBox="0 0 40 34" aria-label="Back"><path d="M12 4 4 12l8 8M4 12h22a10 10 0 0 1 0 20H10" fill="none" stroke="#111" stroke-width="3.5" stroke-linejoin="round"/></svg>
    <div class="title">My Business
      <svg width="20" height="12" viewBox="0 0 20 12"><path d="M0 0h20L10 12z" fill="#111"/></svg>
    </div>
    <svg class="add-booking" width="50" height="50" viewBox="0 0 50 50" aria-label="Add booking"><circle cx="25" cy="25" r="25" fill="#111"/><path d="M25 12v26M12 25h26" stroke="#fff" stroke-width="6"/></svg>
  </header>

  <section class="metric-tiles">
    <div class="metric-tile budget">Budget</div>
    <div class="metric-tile profit">Profit</div>
  </section>

  <nav class="stats-tabs">
    <span class="active">My Stats</span>
    <span class="tab">Efficiency</span>
  </nav>

  <svg class="stats-chart" width="630" height="400" viewBox="0 0 630 400" role="img" aria-label="Weekly budget and profit bar chart">
    <g fill="#9a9a9a" font-size="14" text-anchor="end">
      <text x="60" y="42">$</text>
      <text x="70" y="65">1100</text>
      <text x="70" y="92">1000</text>
      <text x="70" y="147">800</text>
      <text x="70" y="201">600</text>
      <text x="70" y="256">400</text>
      <text x="70" y="310">200</text>
      <text x="70" y="365">0</text>
    </g>
    <g stroke="#dddddd" stroke-width="1">
      <line x1="105" y1="60" x2="600" y2="60"/>
      <line x1="105" y1="142" x2="600" y2="142"/>
      <line x1="105" y1="251" x2="600" y2="251"/>
    </g>
    <g fill="var(--bar-lime)">
      <rect x="120" y="74" width="52" height="286" rx="7"/>
      <rect x="188" y="74" width="52" height="286" rx="7"/>
      <rect x="256" y="120" width="52" height="240" rx="7"/>
      <rect x="324" y="87" width="52" height="273" rx="7"/>
      <rect x="392" y="98" width="52" height="262" rx="7"/>
      <rect x="460" y="19" width="52" height="341" rx="7"/>
      <rect x="528" y="19" width="52" height="341" rx="7"/>
    </g>
    <g fill="var(--bar-green)">
      <rect x="120" y="265" width="52" height="95"/>
      <rect x="188" y="224" width="52" height="136"/>
      <rect x="256" y="251" width="52" height="109"/>
      <rect x="324" y="224" width="52" height="136"/>
      <rect x="392" y="207" width="52" height="153"/>
      <rect x="460" y="243" width="52" height="117"/>
      <rect x="528" y="207" width="52" height="153"/>
    </g>
    <line x1="105" y1="361" x2="600" y2="361" stroke="#111" stroke-width="3"/>
    <g fill="#333" font-size="16" text-anchor="middle">
      <text x="146" y="388">Mon</text>
      <text x="214" y="388">Tue</text>
      <text x="282" y="388">Wed</text>
      <text x="350" y="388">Thu</text>
      <text x="418" y="388">Fri</text>
      <text x="486" y="388">Sat</text>
      <text x="554" y="388">Sun</text>
    </g>
  </svg>

  <nav class="range-filter">
    <span>Today</span>
    <span class="active">Last Week</span>
    <span>Last Month</span>
  </nav>

  <div class="feed-row">
    <span class="label">News:</span>
    <span class="amount">$1000</span>
  </div>
  <div class="feed-row booking">
    <span class="label">New Booking</span>
  </div>

  <nav class="tab-bar">
    <a class="nav-item" aria-label="Home">
      <svg width="54" height="50" viewBox="0 0 54 50"><path d="M27 2 2 24h7v24h14V34h8v14h14V24h7L40 12V4h-6v3z" fill="var(--icon-grey)"/></svg>
    </a>
    <a class="nav-item" aria-label="Calendar">
      <svg width="56" height="52" viewBox="0 0 56 52"><rect x="2" y="6" width="52" height="44" rx="4" fill="var(--icon-grey)"/><rect x="14" y="0" width="6" height="12" rx="2" fill="var(--icon-grey)"/><rect x="36" y="0" width="6" height="12" rx="2" fill="var(--icon-grey)"/><g fill="#ededed"><rect x="8" y="18" width="8" height="7"/><rect x="20" y="18" width="8" height="7"/><rect x="32" y="18" width="8" height="7"/><rect x="44" y="18" width="6" height="7"/><rect x="8" y="29" width="8" height="7"/><rect x="20" y="29" width="8" height="7"/><rect x="32" y="29" width="8" height="7"/><rect x="44" y="29" width="6" height="7"/><rect x="8" y="40" width="8" height="6"/><rect x="20" y="40" width="8" height="6"/><rect x="32" y="40" width="8" height="6"/></g></svg>
    </a>
    <a class="nav-item" aria-label="Bookings">
      <svg width="48" height="48" viewBox="0 0 48 48"><path d="M34 4l10 10L16 42H6V32z" fill="var(--icon-grey)"/><path d="M30 8l10 10M6 32l10 10" stroke="#ededed" stroke-width="2"/></svg>
    </a>
    <a class="nav-item" aria-label="Settings">
      <svg width="52" height="52" viewBox="0 0 52 52"><path d="M8 44 36 16" stroke="var(--icon-grey)" stroke-width="6" stroke-linecap="round"/><path d="M36 16a9 9 0 1 1 10-10l-7 3-1 6 6 1 3-7a9 9 0 0 1-11 7z" fill="var(--icon-grey)"/><path d="M10 6l8 8M18 14l24 26" stroke="var(--icon-grey)" stroke-width="6" stroke-linecap="round"/><path d="M38 36l8 8-4 4-8-8z" fill="var(--icon-grey)"/></svg>
    </a>
  </nav>
</main>
</body>
</html>
```